Website Design for Law Firm

We need a fresh new website design for our client 'Torvek Legal' who specialises as a Criminal, Traffic & Civil Lawyer in Perth, Western Australia. We are looking for a very clean, professional and elegant look for the website, a presence of power and class needed as he deals with high end clients. Black, Silver and hints of gold need to run through the design without making the site look too dark. We are after a very modern, spacious web look, use of large readable text with links to social media (such as Facebook, Google+, Twitter, LinkedIn) to stand out and his contact details to be made very predominate.

Reason: Public holidays here in Australia, need more business hours to discuss designs with client.

Reason: Client needs more time to look through designs.

Reason: Client is going over last of designs. Design will be picked early next week!

Law Firm

```html
<!DOCTYPE html>
<html lang="en">
<head>
<meta charset="utf-8">
<title>Torvek Legal</title>
<link rel="stylesheet" href="https://fonts.googleapis.com/css2?family=Marcellus&family=Marcellus+SC&family=Arimo:ital,wght@0,400;0,700;1,400;1,700&family=Georgia&display=swap">
<style>
:root{
  --ink:#1e1e1e;
  --text:#555;
  --head-top:#f4f4f4;
  --head-bot:#e2e2e2;
  --band:#7a7a7a;
  --band-dark:#5c5c5c;
  --page:#dedede;
  --panel:#f3f3f3;
  --rule:#d4d4d4;
  --gold:#c8721a;
  --gold-light:#f6b23a;
  --footer:#5d5d5d;
  --footer-bar:#2e2e2e;
}
*{box-sizing:border-box;margin:0;padding:0}
html,body{width:851px;height:1200px;overflow:hidden}
body{position:relative;font-family:Arimo,Arial,sans-serif;color:var(--text);background:var(--page)}
.abs{position:absolute}
.header{left:0;top:0;width:851px;height:150px;background:linear-gradient(var(--head-top),var(--head-bot));border-top:4px solid #444}
.brand{left:84px;top:26px;display:flex;align-items:center;gap:8px}
.brand-mark{width:20px;height:20px;background:var(--ink)}
.brand-name{font-family:Marcellus,serif;font-size:30px;color:var(--ink);line-height:1}
.callout{right:84px;top:20px;text-align:right;font-family:"Marcellus SC",serif;color:#333}
.callout .eval{font-size:13px;border-bottom:1px solid #555;padding-bottom:1px;letter-spacing:.5px}
.callout .phone{font-size:19px;margin-top:8px;letter-spacing:1px}
.callout .phone b{font-family:Marcellus,serif;font-weight:400;margin-left:10px}
.callout .email{display:inline-block;margin-top:6px;background:#222;color:#fff;font-size:10px;padding:1px 5px}
.nav{left:85px;top:100px;display:flex;gap:0;font-size:11px;color:#222}
.nav a{color:inherit;text-decoration:none;padding:4px 13px;height:23px}
.nav a.active{background:linear-gradient(#eee,#c9c9c9);border:1px solid #aaa;border-radius:2px;margin-right:13px;padding:4px 7px}
.follow{left:585px;top:100px;display:flex;align-items:center;gap:3px;font-size:11px;color:#666}
.follow span{margin-right:4px}
.social{width:24px;height:24px;border:1px solid #aaa;border-radius:3px;background:linear-gradient(#f4f4f4,#cfcfcf)}
.band{left:0;top:150px;width:851px;height:237px;background:linear-gradient(var(--band-dark),#a8a8a8)}
.hero{left:86px;top:128px;width:684px;height:214px;background:linear-gradient(90deg,#3a2618 0%,#6b4526 35%,#2b1b14 60%,#4a2c1e 100%);box-shadow:0 12px 18px rgba(0,0,0,.35)}
.hero-text{left:98px;top:240px;color:#fff}
.hero-text h1{font-family:Arimo,sans-serif;font-size:21px;font-weight:700;letter-spacing:.5px}
.hero-text p{font-size:10px;line-height:16px;margin-top:4px}
.hero-btn{left:97px;top:301px;width:140px;height:30px;background:linear-gradient(#f0f0f0,#9c9c9c);border:2px solid #666;border-radius:3px;font-size:13px;font-weight:700;color:#333;text-align:center;line-height:26px}
.dots{left:360px;top:362px}
.content{left:85px;top:388px;width:686px;height:645px;background:var(--panel)}
.scroll{left:755px;top:388px;width:16px;height:645px;background:#ececec;border-left:1px solid #ccc}
.scroll .thumb{position:absolute;left:2px;top:18px;width:10px;height:92px;background:#fafafa;border:1px solid #ccc}
.support{left:0;top:372px;width:42px;height:120px;background:linear-gradient(90deg,#e4e4e4,#cfcfcf);border:1px solid #aaa;border-left:none;border-radius:0 4px 4px 0}
.support span{position:absolute;left:5px;top:92px;transform:rotate(-90deg);transform-origin:left top;font-size:10px;color:#555;white-space:nowrap;line-height:12px}
h2{font-family:Marcellus,serif;font-weight:400;color:#222}
.welcome{left:94px;top:398px;font-size:23px}
.welcome-rule{left:94px;top:428px;width:490px;height:1px;background:var(--rule)}
.photo{left:89px;top:445px;width:170px;height:168px;border:4px solid #fff;outline:1px solid #ccc;background:linear-gradient(135deg,#4a2418,#b08a6a 45%,#d9b89a 55%,#3a1a12)}
.intro{left:272px;top:449px;width:318px;font-size:10px;line-height:17px}
.intro p+p{margin-top:16px}
.areas-title{left:97px;top:652px;font-size:19px}
.areas{left:96px;top:684px;width:451px;height:115px;background:#e8e8e8;padding:8px 0 0 8px;display:grid;grid-template-columns:232px 210px;row-gap:11px;font-size:11px;color:#222}
.areas li{list-style:none;display:flex;align-items:center;gap:4px}
.bullet{width:12px;height:12px;border-radius:50%;background:radial-gradient(circle at 40% 35%,var(--gold-light),var(--gold))}
.copy{left:95px;top:817px;width:492px;font-size:10px;line-height:17px}
.copy em{color:var(--gold);font-style:normal}
.news-title{left:97px;top:909px;font-size:19px}
.news-rule{left:97px;top:940px;width:470px;height:1px;background:var(--rule)}
.news{display:flex;gap:10px;width:220px}
.news .thumb{width:40px;height:40px;flex:none;background:linear-gradient(135deg,#f2a04a,#7a3e1a);border:1px solid #ccc}
.news p{font-size:10px;line-height:13px;color:#333}
.news small{display:block;font-family:Georgia,serif;font-style:italic;font-size:8px;color:#555;margin-top:4px}
.news small b{color:#222}
.form{left:595px;top:429px;width:154px;height:595px;background:#e2e2e2;border:1px solid #bbb}
.form .art{height:160px;background:linear-gradient(#f4f4f4,#c9a070 55%,#6b4a2e 85%,#e0e0e0)}
.form h3{position:absolute;left:19px;top:4px;font-family:Marcellus,serif;font-weight:700;font-size:17px;color:#222;line-height:18px}
.form .lede{font-family:Georgia,serif;font-size:8px;font-weight:700;color:#444;padding:0 5px;line-height:12px;margin-top:-6px}
.form label{display:block;font-size:9px;color:#222;margin:9px 5px 4px}
.form .field{margin:0 6px;height:22px;background:#fff;border:1px solid #ccc}
.form .select{margin:0 6px;height:22px;background:linear-gradient(#f2f2f2,#d8d8d8);border:1px solid #bbb;position:relative}
.form .select:after{content:"";position:absolute;right:7px;top:8px;border:4px solid transparent;border-top:6px solid #888}
.form .area{margin:0 6px;height:92px;background:#fff;border:1px solid #ccc}
.send{position:absolute;right:8px;top:482px;width:48px;height:20px;border-radius:3px;background:linear-gradient(#ffd27a,#e08e1e);border:1px solid #b8731a;font-family:Georgia,serif;font-size:11px;font-weight:700;color:#5a2e00;text-align:center;line-height:18px}
.footer{left:0;top:1049px;width:851px;height:151px;background:var(--footer)}
.footbar{left:85px;top:1033px;width:687px;height:32px;background:linear-gradient(#4a4a4a,#141414);display:flex;justify-content:center;align-items:center;font-size:10px;color:#ddd;gap:14px}
.footbar i{font-style:normal;color:#999}
.copyright{left:88px;top:1071px;font-size:8px;color:#ddd}
.visit{left:88px;top:1104px;font-family:Arimo,sans-serif;font-style:italic;font-weight:700;font-size:14px;color:#2a2a2a;line-height:20px}
.address{left:229px;top:1095px;font-size:9px;color:#eee;line-height:12px}
.monogram{left:350px;top:1072px;width:84px;height:124px;background:radial-gradient(#6c6c6c,#5d5d5d 70%)}
.connect{left:477px;top:1101px;font-style:italic;font-weight:700;font-size:14px;color:#2a2a2a;line-height:20px}
.callback{left:600px;top:1090px;font-size:8px;color:#eee;line-height:10px;width:170px}
.callbox{left:597px;top:1118px;width:176px;height:27px;background:linear-gradient(#f4f4f4,#cfcfcf);border-radius:4px;border:1px solid #999}
</style>
</head>
<body>
<header class="abs header">
</header>
<div class="abs brand"><span class="brand-mark"></span><span class="brand-name">Torvek Legal</span></div>
<div class="abs callout">
  <div class="eval">Call for a free evaluation of your case</div>
  <div class="phone">Phone: <b>(555) 210-4837</b></div>
  <div class="email">EMAIL US</div>
</div>
<nav class="abs nav">
  <a class="active">Home</a><a>About Us</a><a>Attorney Profile</a><a>Practice Areas</a><a>Contact Us</a>
</nav>
<div class="abs follow"><span>Folow Us On :</span>
  <i class="social" aria-label="Social link"></i><i class="social" aria-label="Social link"></i><i class="social" aria-label="Social link"></i><i class="social" aria-label="Social link"></i>
</div>

<div class="abs band"></div>
<div class="abs hero" role="img" aria-label="Golden scales of justice and a wooden gavel in front of law books"></div>
<div class="abs hero-text">
  <h1>Know Your Rights !</h1>
  <p>We have industry leading processes and procedures to ensure<br>reliable product. <i>Find out more about our commitment to our cnbmmmn</i></p>
</div>
<div class="abs hero-btn">Free Consultation</div>
<svg class="abs dots" width="131" height="26" viewBox="0 0 131 26">
  <path d="M0 26 C12 26 10 0 24 0 H107 C121 0 119 26 131 26Z" fill="#3a3a3a"/>
  <circle cx="44" cy="12" r="4" fill="#fff"/><circle cx="63" cy="12" r="4" fill="#111"/><circle cx="82" cy="12" r="4" fill="#111"/><circle cx="101" cy="12" r="4" fill="#111"/>
</svg>

<div class="abs support"><span>Free Support<br><b>OFFLINE</b></span></div>

<main class="abs content"></main>
<div class="abs scroll"><div class="thumb"></div></div>

<h2 class="abs welcome">Welcome !</h2>
<div class="abs welcome-rule"></div>
<div class="abs photo" role="img" aria-label="Handshake in front of a shelf of law books"></div>
<div class="abs intro">
  <p>Lorem ipsum dolor sit amet, consectetur adipiscing elit. In interdum aliquet orci, vitae ornare erat elementum et. Nullam sagittis quam in leo ornare ut gravida turpis eleifend. Morbi eget diam non diam iaculis tristique nec nec sem.</p>
  <p>Vestibulum a eros tellus, quis adipiscing neque. Sed varius, risus nec hendrerit pretium, lorem purus euismod risus, tincidunt dictum odio ligula non purus. In volutpat dui a ipsum lobortis rutrum. Pellentesque commodo aliquam pulvinar. In erat risus, molestie vitae porta molestie, pulvinar non justo itae ornare erat elementum et. Nullam sagittis quam in leo ornare ut</p>
</div>

<h2 class="abs areas-title">Areas Of Practice &amp; Legal Services</h2>
<ul class="abs areas">
  <li><i class="bullet"></i>Personal Injury &amp; Civil Litigation</li><li><i class="bullet"></i>Bankruptcy</li>
  <li><i class="bullet"></i>Civil Meditation &amp; Arbitration</li><li><i class="bullet"></i>Criminal Defence</li>
  <li><i class="bullet"></i>Employment Law</li><li><i class="bullet"></i>Malpractice</li>
  <li><i class="bullet"></i>Small Business law</li><li><i class="bullet"></i>Estate Planing &amp; Probate</li>
</ul>
<p class="abs copy">Vestibulum a eros tellus, quis adipiscing neque. <em>Sed varius, risus nec hendrerit pretium, lorem purus euismod risus</em>, tincidunt dictum odio ligula non purus. In volutpat dui a ipsum lobortis rutrum. Pellentesque commodo aliquam pulvinar. <em>In erat risus, molestie vitae porta molestie</em>, pulvinar non justo itae ornare erat elementum et. Nullam sagittis quam in leo ornare ut gravida turpis eleifend. Morbi eget diam non diam iaculis tristique nec nec sem.</p>

<h2 class="abs news-title">Latest News</h2>
<div class="abs news-rule"></div>
<article class="abs news" style="left:98px;top:952px"><div class="thumb" role="img" aria-label="Gavel"></div><p>Westibulum a eros tellus, quis adipiscing neque. Sed varius, risus<small>March 14 2011, <b>42 Comments</b></small></p></article>
<article class="abs news" style="left:385px;top:952px"><div class="thumb" role="img" aria-label="Gavel"></div><p>Westibulum a eros tellus, quis adipiscing neque. Sed varius, risus<small>March 14 2011, <b>42 Comments</b></small></p></article>

<aside class="abs form">
  <div class="art" role="img" aria-label="Open law book beside golden scales"></div>
  <h3>Free<br>Consultation</h3>
  <p class="lede">Integer a sapien id diam temore unt Ut cursus nisl vel orci tristiqu eros sum</p>
  <label>*Name :</label><div class="field"></div>
  <label>*Phone Number :</label><div class="field"></div>
  <label>*Email Addres :</label><div class="field"></div>
  <label>*Consultation In :</label><div class="select"></div>
  <label>*Questions and comments :</label><div class="area"></div>
  <div class="send">Send</div>
</aside>

<footer class="abs footer"></footer>
<nav class="abs footbar"><span>Home</span><i>I</i><span>About Us</span><i>I</i><span>Attorney Profile</span><i>I</i><span>Practice Areas</span><i>I</i><span>Contact Us</span></nav>
<div class="abs copyright">Copyright 2014 Torvek Legal</div>
<div class="abs visit">Come Visit Us<br>At Our Office !</div>
<svg class="abs" style="left:187px;top:1110px" width="30" height="28" viewBox="0 0 30 28"><path d="M2 2 L14 14 L2 26 M14 2 L26 14 L14 26" fill="none" stroke="#bbb" stroke-width="5"/></svg>
<address class="abs address" style="font-style:normal">58 Harlow Lane, Suite 12,<br>Perth, WA 6000<br>Australia<br>Phone : 1-555-014-382<br>Fax : 1-555-019-2240</address>
<div class="abs monogram"></div>
<div class="abs connect">We'd have to<br>connect with you :</div>
<div class="abs callback">Enter your number and we will call you<br>to anwer any questions</div>
<div class="abs callbox"></div>
<svg class="abs" style="left:606px;top:1124px" width="166" height="16" viewBox="0 0 166 16">
  <rect x="1" y="1" width="36" height="14" rx="7" fill="#ddd" stroke="#999"/>
  <rect x="42" y="1" width="40" height="14" rx="7" fill="#ddd" stroke="#999"/>
  <rect x="87" y="1" width="44" height="14" rx="7" fill="#ddd" stroke="#999"/>
  <line x1="137" y1="-4" x2="137" y2="20" stroke="#999"/>
  <path d="M146 4 h14 v3 h-3 l-1-2 h-6 l-1 2 h-3z M147 9 h12 v5 h-12z" fill="#333"/>
</svg>
</body>
</html>
```